Industrial Professional Business Card Design (Vantrel Systems)

Would like professional looking business cards. Not too busy leaning towards minimal. Should have a slogan like:
"Industrial Automation and Control".

We are a tech company that programs industrial PLC computers. We also develop custom hardware solutions. Please use the logo for inspiration.

Target Market(s)

Mining, industrial, processing, automation, factory

Industry/Entity Type

Engineering

Contact Information for Business Card

Name, phone, email, website. job title.

Font styles to use
Other font styles liked:
• droid sans

Requirements
Must have
• Use colours that go well with the logo. Not too busy design.

```html
<!DOCTYPE html>
<html lang="en">
<head>
<meta charset="utf-8">
<title>Vantrel Systems – Business Card</title>
<link href="https://fonts.googleapis.com/css2?family=Montserrat:wght@700&family=Open+Sans:wght@400;600&family=Josefin+Slab:wght@400&display=swap" rel="stylesheet">
<style>
  :root {
    --navy: #1d4b75;
    --orange: #f26a1b;
    --white: #ffffff;
    --stage: #2a2a2a;
  }
  * { box-sizing: border-box; margin: 0; padding: 0; }
  html, body {
    width: 1200px; height: 1015px; overflow: hidden;
    background: var(--stage);
  }
  .sheet {
    position: relative; width: 1200px; height: 1015px;
  }
  .card {
    position: absolute; left: 250px; width: 700px; height: 400px;
    background: var(--navy); overflow: hidden;
    box-shadow: 0 12px 30px rgba(0,0,0,0.45);
  }
  .card--front { top: 70px; }
  .card--back { top: 545px; }

  /* Front */
  .front-brand {
    position: absolute; inset: 0;
    display: flex; flex-direction: column; align-items: center; justify-content: center;
    gap: 14px;
  }
  .brand-line { display: flex; align-items: center; gap: 18px; }
  .brand-dot {
    width: 44px; height: 44px; border-radius: 50%; background: var(--orange);
  }
  .brand-name {
    font-family: "Josefin Slab", serif; font-weight: 400;
    font-size: 62px; color: var(--white); letter-spacing: 1px; line-height: 1;
  }
  .slogan {
    font-family: "Montserrat", sans-serif; font-weight: 700;
    font-size: 17px; color: var(--white); letter-spacing: 0.5px; text-transform: uppercase;
  }

  /* Back */
  .back-art { position: absolute; inset: 0; }
  .back-brand {
    position: absolute; left: 400px; top: 150px; width: 280px;
    display: flex; flex-direction: column; align-items: center; gap: 14px;
  }
  .back-brand .brand-dot { width: 36px; height: 36px; }
  .back-brand .brand-name { color: var(--navy); font-size: 38px; text-align: center; }
  .person { position: absolute; left: 60px; top: 120px; }
  .person-name {
    font-family: "Montserrat", sans-serif; font-weight: 700;
    font-size: 22px; color: var(--orange); text-transform: uppercase; letter-spacing: 0.5px;
  }
  .person-title {
    font-family: "Open Sans", sans-serif; font-size: 18px; color: var(--white); margin-top: 2px;
  }
  .contact-list {
    position: absolute; left: 60px; top: 235px; list-style: none;
    display: flex; flex-direction: column; gap: 10px;
  }
  .contact-item {
    display: flex; align-items: center; gap: 12px;
    font-family: "Open Sans", sans-serif; font-size: 17px; color: var(--white);
  }
  .contact-icon { width: 20px; height: 20px; flex: none; }
</style>
</head>
<body>
<main class="sheet">
  <section class="card card--front" aria-label="Card front">
    <div class="front-brand">
      <div class="brand-line">
        <span class="brand-dot"></span>
        <span class="brand-name">Vantrel Systems</span>
      </div>
      <p class="slogan">Industrial Automation and Control</p>
    </div>
  </section>

  <section class="card card--back" aria-label="Card back">
    <svg class="back-art" width="700" height="400" viewBox="0 0 700 400" aria-hidden="true">
      <circle cx="555" cy="160" r="232" fill="none" stroke="var(--orange)" stroke-width="5"/>
      <circle cx="575" cy="150" r="232" fill="var(--white)"/>
    </svg>
    <div class="back-brand">
      <span class="brand-dot"></span>
      <span class="brand-name">Vantrel Systems</span>
    </div>

    <div class="person">
      <p class="person-name">Daniel Harrow</p>
      <p class="person-title">Managing Director</p>
    </div>

    <ul class="contact-list">
      <li class="contact-item">
        <svg class="contact-icon" viewBox="0 0 24 24" aria-hidden="true"><path fill="var(--orange)" d="M6.6 10.8a15 15 0 0 0 6.6 6.6l2.2-2.2a1 1 0 0 1 1-.25 11.4 11.4 0 0 0 3.6.57 1 1 0 0 1 1 1V20a1 1 0 0 1-1 1A17 17 0 0 1 3 4a1 1 0 0 1 1-1h3.5a1 1 0 0 1 1 1c0 1.25.2 2.45.57 3.6a1 1 0 0 1-.25 1z"/></svg>
        044-987 654 321
      </li>
      <li class="contact-item">
        <svg class="contact-icon" viewBox="0 0 24 24" aria-hidden="true"><rect x="2" y="5" width="20" height="14" rx="1" fill="var(--orange)"/><path d="M2.5 6l9.5 7 9.5-7" fill="none" stroke="var(--navy)" stroke-width="1.6"/></svg>
        info@vantrelsystems.com
      </li>
      <li class="contact-item">
        <svg class="contact-icon" viewBox="0 0 24 24" aria-hidden="true"><g fill="none" stroke="var(--orange)" stroke-width="2"><circle cx="12" cy="12" r="9.5"/><ellipse cx="12" cy="12" rx="4" ry="9.5"/><path d="M2.5 12h19M4 7h16M4 17h16"/></g></svg>
        www.vantrelsystems.com
      </li>
    </ul>
  </section>
</main>
</body>
</html>
```